App Design Project

Hello,
I'm looking for a great designer for my iOS Applications, we have a lot of works and we're short in designers :(
I want to revamp my thermometer iOS app. You will find attached the images I want to replace. I need something with the same element (temp, condition, weather icon) but with a different look!
Same, new icon, you have carte blanche to this one.
I want a design that stands out from the hundreds of weather application that almost all the same design. I am looking for something that does say "wow, it rocks."
Please do not Provide classic design that we can see everywhere ... I'm looking for something with a real artistic choice, contrast, colours, etc.
As a marketing screenshot, I want something classic, you'll find an example attached, feel free to innovate.
To sum-up :
- One new view for my App
- One new icon
- One marketing screenshot
Marketing

```html
<!DOCTYPE html>
<html lang="en">
<head>
<meta charset="utf-8">
<title>Weather App Screens</title>
<link rel="stylesheet" href="https://fonts.googleapis.com/css2?family=Francois+One&family=Oswald:wght@200;400;600&display=swap">
<style>
  :root {
    --canvas: #2b9fe6;
    --strip: #2a9be3;
    --strip-line: #6cc3f5;
    --band: #1d2127;
    --ring: #2d9ee8;
    --white: #ffffff;
    --ink: #1a1d22;
    --sun: #ffd21e;
    --sun-edge: #e9a412;
    --cloud: #ffffff;
    --cloud-edge: #c9d3dc;
  }
  * { box-sizing: border-box; margin: 0; padding: 0; }
  html, body { width: 1200px; height: 900px; overflow: hidden; }
  body {
    background: var(--canvas);
    position: relative;
    font-family: "Oswald", sans-serif;
    color: var(--white);
  }
  .screen {
    position: absolute;
    width: 172px;
    display: grid;
    grid-template-rows: 1fr 56px 48px;
    overflow: hidden;
    box-shadow: 0 0 0 1px rgba(0,0,0,.15);
  }
  .row-top { top: 78px; height: 312px; }
  .row-bottom { top: 543px; height: 284px; }
  .col-1 { left: 52px; }
  .col-2 { left: 273px; }
  .col-3 { left: 494px; }
  .col-4 { left: 713px; }
  .col-5 { left: 946px; }

  .sky { position: relative; display: flex; flex-direction: column; align-items: center; }
  .backdrop { position: absolute; inset: 0; }
  .condition, .condition-icon, .reading, .unit-toggle { position: relative; }
  .condition {
    font-family: "Francois One", sans-serif;
    font-weight: 400;
    font-size: 20px;
    margin-top: 28px;
    text-shadow: 0 1px 3px rgba(0,0,0,.45);
    letter-spacing: .2px;
    white-space: nowrap;
  }
  .row-bottom .condition { margin-top: 24px; }
  .condition-icon { width: 48px; height: 40px; margin-top: 18px; }
  .row-bottom .condition-icon { margin-top: 10px; }
  .reading {
    display: flex; align-items: center; gap: 4px;
    font-weight: 200; font-size: 44px; line-height: 1;
    margin-top: 6px; margin-left: -8px;
  }
  .reading sup { font-size: 20px; vertical-align: top; position: relative; top: -10px; }
  .reading .unit { font-size: 40px; }
  .thermo { width: 14px; height: 36px; }
  .unit-toggle {
    position: absolute; right: 10px; bottom: 16px;
    width: 22px; height: 10px; border-radius: 5px;
    background: var(--ring); font-size: 5px; line-height: 10px; padding-left: 4px;
  }
  .unit-toggle::after {
    content: ""; position: absolute; right: 1px; top: 1px;
    width: 8px; height: 8px; border-radius: 50%; background: var(--white);
  }
  .row-bottom .sky .unit-toggle { bottom: 10px; }

  .gauges {
    background: var(--band);
    display: flex; justify-content: space-between; align-items: center;
    padding: 0 20px 0 22px;
  }
  .gauge { width: 36px; height: 36px; overflow: visible; }

  .forecast {
    list-style: none; background: var(--strip);
    display: grid; grid-template-columns: repeat(4, 1fr);
    padding: 6px 2px 0; border-top: 1px solid var(--strip-line);
  }
  .day { display: flex; flex-direction: column; align-items: center; font-size: 6px; line-height: 1.25; }
  .day-name { letter-spacing: .3px; }
  .day-icon { width: 13px; height: 10px; margin: 1px 0; }
  .day-temp { font-weight: 600; font-size: 5px; }

  .screen--clear .backdrop { background: linear-gradient(180deg, #2f86d8 0%, #6bb6ef 55%, #cfe6f8 100%); }
  .screen--partly .backdrop { background: radial-gradient(circle at 30% 30%, #f2f5f8 0 18%, transparent 40%), linear-gradient(180deg, #3d6fa8, #9bb6d3 60%, #e6edf3); }
  .screen--rain .backdrop { background: linear-gradient(160deg, #d8d9c8 0%, #9aa392 40%, #3d4a45 100%); }
  .screen--hail .backdrop { background: linear-gradient(180deg, #7c8590 0%, #5a6168 50%, #8c9195 100%); }
  .screen--overcast .backdrop { background: linear-gradient(180deg, #3a4656 0%, #55657a 50%, #7e8a98 100%); }
  .screen--fog .backdrop { background: linear-gradient(180deg, #c3c4c4 0%, #a7a9a9 60%, #7d8080 100%); }
  .screen--storm .backdrop { background: linear-gradient(170deg, #1f3d44 0%, #3c6a6c 50%, #2a4548 100%); }
  .screen--haze .backdrop { background: linear-gradient(180deg, #c7c9c8 0%, #9da3a2 55%, #5f6866 100%); }
  .screen--mostly .backdrop { background: linear-gradient(180deg, #4a4d52 0%, #9a9ea3 50%, #5a5e63 100%); }
  .screen--wind .backdrop { background: linear-gradient(180deg, #7d8aa8 0%, #b6a9b4 45%, #3d4348 100%); }
  .screen .sky .condition-icon, .screen .sky .reading { filter: drop-shadow(0 1px 2px rgba(0,0,0,.25)); }
</style>
</head>
<body>

<svg width="0" height="0" style="position:absolute" aria-hidden="true">
  <defs>
    <symbol id="i-cloud" viewBox="0 0 48 40">
      <path d="M12 32 a8 8 0 0 1 1-16 a11 11 0 0 1 21-3 a9 9 0 0 1 3 19 z" fill="#ffffff" stroke="#c9d3dc" stroke-width="1"/>
    </symbol>
    <symbol id="i-sun" viewBox="0 0 48 40">
      <circle cx="24" cy="20" r="15" fill="#ffd21e" stroke="#e9a412" stroke-width="1.5"/>
    </symbol>
    <symbol id="i-partly" viewBox="0 0 48 40">
      <circle cx="20" cy="16" r="12" fill="#ffd21e" stroke="#e9a412" stroke-width="1.5"/>
      <path d="M18 36 a6 6 0 0 1 1-12 a8 8 0 0 1 15-2 a7 7 0 0 1 3 14 z" fill="#ffffff" stroke="#c9d3dc" stroke-width="1"/>
    </symbol>
    <symbol id="i-rain" viewBox="0 0 48 40">
      <path d="M10 26 a7 7 0 0 1 1-14 a10 10 0 0 1 19-3 a8 8 0 0 1 3 17 z" fill="#ffffff" stroke="#c9d3dc" stroke-width="1"/>
      <path d="M16 30 v4 M23 31 v4 M30 30 v4" stroke="#ffffff" stroke-width="1.6" stroke-linecap="round"/>
    </symbol>
    <symbol id="i-storm" viewBox="0 0 48 40">
      <path d="M10 26 a7 7 0 0 1 1-14 a10 10 0 0 1 19-3 a8 8 0 0 1 3 17 z" fill="#ffffff" stroke="#c9d3dc" stroke-width="1"/>
      <path d="M16 29 v3 M20 31 v3" stroke="#4aa3e8" stroke-width="1.6" stroke-linecap="round"/>
      <path d="M27 28 l-3 6 h3 l-2 5 l6-7 h-3 l2-4 z" fill="#3b7fd6"/>
    </symbol>
    <symbol id="i-fog" viewBox="0 0 48 40">
      <path d="M8 24 a6 6 0 0 1 1-12 a9 9 0 0 1 17-2 a7 7 0 0 1 2 14 z" fill="#d9dcdd" stroke="#aeb3b5" stroke-width="1"/>
      <path d="M18 34 a6 6 0 0 1 1-12 a9 9 0 0 1 17-2 a7 7 0 0 1 2 14 z" fill="#e7e9ea" stroke="#aeb3b5" stroke-width="1"/>
    </symbol>
    <symbol id="i-thermo" viewBox="0 0 14 36">
      <path d="M4 5 a3 3 0 0 1 6 0 v19 a6 6 0 1 1 -6 0 z" fill="none" stroke="#ffffff" stroke-width="1.6"/>
      <circle cx="7" cy="29" r="3" fill="#ffffff"/>
      <path d="M7 10 v18" stroke="#ffffff" stroke-width="2"/>
    </symbol>
    <symbol id="g-humidity" viewBox="0 0 36 36">
      <circle cx="18" cy="18" r="13" fill="#2a2f36"/>
      <path d="M18 3 A15 15 0 1 1 5 25.5" fill="none" stroke="#2d9ee8" stroke-width="2"/>
      <path d="M5 25.5 A15 15 0 0 1 18 3" fill="none" stroke="#3a4048" stroke-width="2"/>
      <path d="M18 10 c3 4 5 6 5 8.5 a5 5 0 0 1 -10 0 c0-2.5 2-4.5 5-8.5 z" fill="#e6e6e6"/>
      <text x="18" y="28" text-anchor="middle" font-family="Oswald, sans-serif" font-size="4.5" font-weight="600" fill="#ffffff">60%</text>
    </symbol>
    <symbol id="g-wind" viewBox="0 0 36 36">
      <circle cx="18" cy="18" r="12" fill="#2a2f36"/>
      <path d="M18 4 A14 14 0 0 1 32 18" fill="none" stroke="#2d9ee8" stroke-width="2"/>
      <path d="M13 15 h8 a2 2 0 1 0 -2-2 M13 18 h10 a2 2 0 1 1 -2 2" fill="none" stroke="#e6e6e6" stroke-width="1.1"/>
      <text x="18" y="2.6" text-anchor="middle" font-family="Oswald, sans-serif" font-size="3.6" fill="#ffffff">N</text>
      <text x="1.8" y="19.3" text-anchor="middle" font-family="Oswald, sans-serif" font-size="3.6" fill="#ffffff">E</text>
      <text x="34.2" y="19.3" text-anchor="middle" font-family="Oswald, sans-serif" font-size="3.6" fill="#ffffff">W</text>
      <text x="18" y="35.4" text-anchor="middle" font-family="Oswald, sans-serif" font-size="3.6" fill="#ffffff">S</text>
      <text x="18" y="26" text-anchor="middle" font-family="Oswald, sans-serif" font-size="3.8" font-weight="600" fill="#ffffff">40km/hr</text>
    </symbol>
  </defs>
</svg>

<!-- Top row -->
<article class="screen screen--clear row-top col-1">
  <div class="sky">
    <div class="backdrop" role="img" aria-label="Photo of a bright blue sky with light clouds"></div>
    <h2 class="condition">Clear</h2>
    <svg class="condition-icon"><use href="#i-sun"/></svg>
    <p class="reading"><svg class="thermo"><use href="#i-thermo"/></svg>-12<sup>°</sup><span class="unit">c</span></p>
    <span class="unit-toggle">°C</span>
  </div>
  <div class="gauges"><svg class="gauge" viewBox="0 0 36 36"><use href="#g-humidity"/></svg><svg class="gauge" viewBox="0 0 36 36"><use href="#g-wind"/></svg></div>
  <ul class="forecast">
    <li class="day"><span class="day-name">MON</span><svg class="day-icon"><use href="#i-partly"/></svg><span class="day-temp">▲25°</span><span class="day-temp">▼19°</span></li>
    <li class="day"><span class="day-name">TUES</span><svg class="day-icon"><use href="#i-cloud"/></svg><span class="day-temp">▲19°</span><span class="day-temp">▼14°</span></li>
    <li class="day"><span class="day-name">WEDS</span><svg class="day-icon"><use href="#i-rain"/></svg><span class="day-temp">▲12°</span><span class="day-temp">▼6°</span></li>
    <li class="day"><span class="day-name">THURS</span><svg class="day-icon"><use href="#i-partly"/></svg><span class="day-temp">▲25°</span><span class="day-temp">▼19°</span></li>
  </ul>
</article>

<article class="screen screen--partly row-top col-2">
  <div class="sky">
    <div class="backdrop" role="img" aria-label="Photo of blue sky with large white clouds"></div>
    <h2 class="condition">Partly Cloudy</h2>
    <svg class="condition-icon"><use href="#i-partly"/></svg>
    <p class="reading"><svg class="thermo"><use href="#i-thermo"/></svg>-12<sup>°</sup><span class="unit">c</span></p>
    <span class="unit-toggle">°C</span>
  </div>
  <div class="gauges"><svg class="gauge" viewBox="0 0 36 36"><use href="#g-humidity"/></svg><svg class="gauge" viewBox="0 0 36 36"><use href="#g-wind"/></svg></div>
  <ul class="forecast">
    <li class="day"><span class="day-name">MON</span><svg class="day-icon"><use href="#i-partly"/></svg><span class="day-temp">▲25°</span><span class="day-temp">▼19°</span></li>
    <li class="day"><span class="day-name">TUES</span><svg class="day-icon"><use href="#i-cloud"/></svg><span class="day-temp">▲19°</span><span class="day-temp">▼14°</span></li>
    <li class="day"><span class="day-name">WEDS</span><svg class="day-icon"><use href="#i-rain"/></svg><span class="day-temp">▲12°</span><span class="day-temp">▼6°</span></li>
    <li class="day"><span class="day-name">THURS</span><svg class="day-icon"><use href="#i-partly"/></svg><span class="day-temp">▲25°</span><span class="day-temp">▼19°</span></li>
  </ul>
</article>

<article class="screen screen--rain row-top col-3">
  <div class="sky">
    <div class="backdrop" role="img" aria-label="Photo of raindrops on a window pane"></div>
    <h2 class="condition">Rain</h2>
    <svg class="condition-icon"><use href="#i-rain"/></svg>
    <p class="reading"><svg class="thermo"><use href="#i-thermo"/></svg>-12<sup>°</sup><span class="unit">c</span></p>
    <span class="unit-toggle">°C</span>
  </div>
  <div class="gauges"><svg class="gauge" viewBox="0 0 36 36"><use href="#g-humidity"/></svg><svg class="gauge" viewBox="0 0 36 36"><use href="#g-wind"/></svg></div>
  <ul class="forecast">
    <li class="day"><span class="day-name">MON</span><svg class="day-icon"><use href="#i-partly"/></svg><span class="day-temp">▲25°</span><span class="day-temp">▼19°</span></li>
    <li class="day"><span class="day-name">TUES</span><svg class="day-icon"><use href="#i-cloud"/></svg><span class="day-temp">▲19°</span><span class="day-temp">▼14°</span></li>
    <li class="day"><span class="day-name">WEDS</span><svg class="day-icon"><use href="#i-rain"/></svg><span class="day-temp">▲12°</span><span class="day-temp">▼6°</span></li>
    <li class="day"><span class="day-name">THURS</span><svg class="day-icon"><use href="#i-partly"/></svg><span class="day-temp">▲25°</span><span class="day-temp">▼19°</span></li>
  </ul>
</article>

<article class="screen screen--hail row-top col-4">
  <div class="sky">
    <div class="backdrop" role="img" aria-label="Photo of a street covered in hailstones"></div>
    <h2 class="condition">Hail</h2>
    <svg class="condition-icon"><use href="#i-rain"/></svg>
    <p class="reading"><svg class="thermo"><use href="#i-thermo"/></svg>-12<sup>°</sup><span class="unit">c</span></p>
    <span class="unit-toggle">°C</span>
  </div>
  <div class="gauges"><svg class="gauge" viewBox="0 0 36 36"><use href="#g-humidity"/></svg><svg class="gauge" viewBox="0 0 36 36"><use href="#g-wind"/></svg></div>
  <ul class="forecast">
    <li class="day"><span class="day-name">MON</span><svg class="day-icon"><use href="#i-partly"/></svg><span class="day-temp">▲25°</span><span class="day-temp">▼19°</span></li>
    <li class="day"><span class="day-name">TUES</span><svg class="day-icon"><use href="#i-cloud"/></svg><span class="day-temp">▲19°</span><span class="day-temp">▼14°</span></li>
    <li class="day"><span class="day-name">WEDS</span><svg class="day-icon"><use href="#i-rain"/></svg><span class="day-temp">▲12°</span><span class="day-temp">▼6°</span></li>
    <li class="day"><span class="day-name">THURS</span><svg class="day-icon"><use href="#i-partly"/></svg><span class="day-temp">▲25°</span><span class="day-temp">▼19°</span></li>
  </ul>
</article>

<article class="screen screen--overcast row-top col-5">
  <div class="sky">
    <div class="backdrop" role="img" aria-label="Photo of a heavy dark overcast sky"></div>
    <h2 class="condition">Overcast</h2>
    <svg class="condition-icon"><use href="#i-cloud"/></svg>
    <p class="reading"><svg class="thermo"><use href="#i-thermo"/></svg>-12<sup>°</sup><span class="unit">c</span></p>
    <span class="unit-toggle">°C</span>
  </div>
  <div class="gauges"><svg class="gauge" viewBox="0 0 36 36"><use href="#g-humidity"/></svg><svg class="gauge" viewBox="0 0 36 36"><use href="#g-wind"/></svg></div>
  <ul class="forecast">
    <li class="day"><span class="day-name">MON</span><svg class="day-icon"><use href="#i-partly"/></svg><span class="day-temp">▲25°</span><span class="day-temp">▼19°</span></li>
    <li class="day"><span class="day-name">TUES</span><svg class="day-icon"><use href="#i-cloud"/></svg><span class="day-temp">▲19°</span><span class="day-temp">▼14°</span></li>
    <li class="day"><span class="day-name">WEDS</span><svg class="day-icon"><use href="#i-rain"/></svg><span class="day-temp">▲12°</span><span class="day-temp">▼6°</span></li>
    <li class="day"><span class="day-name">THURS</span><svg class="day-icon"><use href="#i-partly"/></svg><span class="day-temp">▲25°</span><span class="day-temp">▼19°</span></li>
  </ul>
</article>

<!-- Bottom row -->
<article class="screen screen--fog row-bottom col-1">
  <div class="sky">
    <div class="backdrop" role="img" aria-label="Photo of a foggy lake with bare branches"></div>
    <h2 class="condition">Fog</h2>
    <svg class="condition-icon"><use href="#i-fog"/></svg>
    <p class="reading"><svg class="thermo"><use href="#i-thermo"/></svg>-12<sup>°</sup><span class="unit">c</span></p>
    <span class="unit-toggle">°C</span>
  </div>
  <div class="gauges"><svg class="gauge" viewBox="0 0 36 36"><use href="#g-humidity"/></svg><svg class="gauge" viewBox="0 0 36 36"><use href="#g-wind"/></svg></div>
  <ul class="forecast">
    <li class="day"><span class="day-name">MON</span><svg class="day-icon"><use href="#i-partly"/></svg><span class="day-temp">▲25°</span><span class="day-temp">▼19°</span></li>
    <li class="day"><span class="day-name">TUES</span><svg class="day-icon"><use href="#i-cloud"/></svg><span class="day-temp">▲19°</span><span class="day-temp">▼14°</span></li>
    <li class="day"><span class="day-name">WEDS</span><svg class="day-icon"><use href="#i-rain"/></svg><span class="day-temp">▲12°</span><span class="day-temp">▼6°</span></li>
    <li class="day"><span class="day-name">THURS</span><svg class="day-icon"><use href="#i-partly"/></svg><span class="day-temp">▲25°</span><span class="day-temp">▼19°</span></li>
  </ul>
</article>

<article class="screen screen--storm row-bottom col-2">
  <div class="sky">
    <div class="backdrop" role="img" aria-label="Photo of a stormy sky with a lightning strike"></div>
    <h2 class="condition">Thunderstorm</h2>
    <svg class="condition-icon"><use href="#i-storm"/></svg>
    <p class="reading"><svg class="thermo"><use href="#i-thermo"/></svg>-12<sup>°</sup><span class="unit">c</span></p>
    <span class="unit-toggle">°C</span>
  </div>
  <div class="gauges"><svg class="gauge" viewBox="0 0 36 36"><use href="#g-humidity"/></svg><svg class="gauge" viewBox="0 0 36 36"><use href="#g-wind"/></svg></div>
  <ul class="forecast">
    <li class="day"><span class="day-name">MON</span><svg class="day-icon"><use href="#i-partly"/></svg><span class="day-temp">▲25°</span><span class="day-temp">▼19°</span></li>
    <li class="day"><span class="day-name">TUES</span><svg class="day-icon"><use href="#i-cloud"/></svg><span class="day-temp">▲19°</span><span class="day-temp">▼14°</span></li>
    <li class="day"><span class="day-name">WEDS</span><svg class="day-icon"><use href="#i-rain"/></svg><span class="day-temp">▲12°</span><span class="day-temp">▼6°</span></li>
    <li class="day"><span class="day-name">THURS</span><svg class="day-icon"><use href="#i-partly"/></svg><span class="day-temp">▲25°</span><span class="day-temp">▼19°</span></li>
  </ul>
</article>

<article class="screen screen--haze row-bottom col-3">
  <div class="sky">
    <div class="backdrop" role="img" aria-label="Photo of a city skyline in haze"></div>
    <h2 class="condition">Haze</h2>
    <svg class="condition-icon"><use href="#i-cloud"/></svg>
    <p class="reading"><svg class="thermo"><use href="#i-thermo"/></svg>-12<sup>°</sup><span class="unit">c</span></p>
    <span class="unit-toggle">°C</span>
  </div>
  <div class="gauges"><svg class="gauge" viewBox="0 0 36 36"><use href="#g-humidity"/></svg><svg class="gauge" viewBox="0 0 36 36"><use href="#g-wind"/></svg></div>
  <ul class="forecast">
    <li class="day"><span class="day-name">MON</span><svg class="day-icon"><use href="#i-partly"/></svg><span class="day-temp">▲25°</span><span class="day-temp">▼19°</span></li>
    <li class="day"><span class="day-name">TUES</span><svg class="day-icon"><use href="#i-cloud"/></svg><span class="day-temp">▲19°</span><span class="day-temp">▼14°</span></li>
    <li class="day"><span class="day-name">WEDS</span><svg class="day-icon"><use href="#i-rain"/></svg><span class="day-temp">▲12°</span><span class="day-temp">▼6°</span></li>
    <li class="day"><span class="day-name">THURS</span><svg class="day-icon"><use href="#i-partly"/></svg><span class="day-temp">▲25°</span><span class="day-temp">▼19°</span></li>
  </ul>
</article>

<article class="screen screen--mostly row-bottom col-4">
  <div class="sky">
    <div class="backdrop" role="img" aria-label="Photo of a sky filled with grey and white clouds"></div>
    <h2 class="condition">Mostly Cloudy</h2>
    <svg class="condition-icon"><use href="#i-cloud"/></svg>
    <p class="reading"><svg class="thermo"><use href="#i-thermo"/></svg>-12<sup>°</sup><span class="unit">c</span></p>
    <span class="unit-toggle">°C</span>
  </div>
  <div class="gauges"><svg class="gauge" viewBox="0 0 36 36"><use href="#g-humidity"/></svg><svg class="gauge" viewBox="0 0 36 36"><use href="#g-wind"/></svg></div>
  <ul class="forecast">
    <li class="day"><span class="day-name">MON</span><svg class="day-icon"><use href="#i-partly"/></svg><span class="day-temp">▲25°</span><span class="day-temp">▼19°</span></li>
    <li class="day"><span class="day-name">TUES</span><svg class="day-icon"><use href="#i-cloud"/></svg><span class="day-temp">▲19°</span><span class="day-temp">▼14°</span></li>
    <li class="day"><span class="day-name">WEDS</span><svg class="day-icon"><use href="#i-rain"/></svg><span class="day-temp">▲12°</span><span class="day-temp">▼6°</span></li>
    <li class="day"><span class="day-name">THURS</span><svg class="day-icon"><use href="#i-partly"/></svg><span class="day-temp">▲25°</span><span class="day-temp">▼19°</span></li>
  </ul>
</article>

<article class="screen screen--wind row-bottom col-5">
  <div class="sky">
    <div class="backdrop" role="img" aria-label="Photo of palm trees bending in strong wind"></div>
    <h2 class="condition">Wind</h2>
    <svg class="condition-icon"><use href="#i-cloud"/></svg>
    <p class="reading"><svg class="thermo"><use href="#i-thermo"/></svg>-12<sup>°</sup><span class="unit">c</span></p>
    <span class="unit-toggle">°C</span>
  </div>
  <div class="gauges"><svg class="gauge" viewBox="0 0 36 36"><use href="#g-humidity"/></svg><svg class="gauge" viewBox="0 0 36 36"><use href="#g-wind"/></svg></div>
  <ul class="forecast">
    <li class="day"><span class="day-name">MON</span><svg class="day-icon"><use href="#i-partly"/></svg><span class="day-temp">▲25°</span><span class="day-temp">▼19°</span></li>
    <li class="day"><span class="day-name">TUES</span><svg class="day-icon"><use href="#i-cloud"/></svg><span class="day-temp">▲19°</span><span class="day-temp">▼14°</span></li>
    <li class="day"><span class="day-name">WEDS</span><svg class="day-icon"><use href="#i-rain"/></svg><span class="day-temp">▲12°</span><span class="day-temp">▼6°</span></li>
    <li class="day"><span class="day-name">THURS</span><svg class="day-icon"><use href="#i-partly"/></svg><span class="day-temp">▲25°</span><span class="day-temp">▼19°</span></li>
  </ul>
</article>

</body>
</html>
```